Veloria Energy (Alternative Energy)

We sell solar panels and geothermal heating and cooling applications.
We want to emphasize that we can offer AFFORDABLE solar and thermal heating applications.
Governmental 30% tax rebate if ordered by 2017.
Solar panels from 40 -90% efficient
Units pay for themselves
Can be used with current (existing) water and heating systems
Lower energy consumption
Great Backup Heaters in case of power outage.
100% solar powered units. Self running thermosphyin design
Low maintenance
Can be Self installed
Saves the environment
Zero Emissions
Increases homes resale value
Great for remote locations
Increases Jobs

Target Market(s)

V.E.

Industry/Entity Type

Solar

Logo Text

The future is here

Number of Pages Required

5+ page

Font styles to use
Serif

Colors
f37122
fbee3e
acd036
ffffff
000000

Requirements
Must have
• Emphasize that we can offer affordable solar and thermal heating applications
• Pays for themselves within 1-3 years
• Solar panels from 40 -90% efficient
• 100% sustainable and renewable
• Very little sun light required
Nice to have
• Very professional clean modern web design
• Needs to achieve sales results.
Should not have
• any lingo. or confusion. Must be simple and effective. Needs to achieve sales results.

```html
<!DOCTYPE html>
<html lang="en">
<head>
<meta charset="utf-8">
<title>Veloria Energy</title>
<link href="https://fonts.googleapis.com/css2?family=Open+Sans:wght@400;600;700&display=swap" rel="stylesheet">
<style>
:root{
  --orange:#f37122;
  --yellow:#fbee3e;
  --green:#acd036;
  --white:#ffffff;
  --black:#000000;
  --ink:#333333;
  --muted:#777777;
  --band:#e9e9e9;
  --footer:#2b2b2b;
  --footer-deep:#1f1f1f;
}
*{margin:0;padding:0;box-sizing:border-box}
html,body{width:673px;height:1200px;overflow:hidden;background:var(--white);font-family:"Open Sans",Arial,sans-serif;color:var(--ink)}
.page{width:673px;height:1200px;position:relative}

.site-header{height:60px;display:flex;align-items:center;justify-content:space-between;padding:0 18px 0 26px}
.brand{display:flex;align-items:center;gap:8px;font-size:21px;font-weight:600;color:var(--ink)}
.brand-dot{width:12px;height:12px;border-radius:50%;background:var(--orange)}
.main-nav{display:flex;gap:4px}
.main-nav a{font-size:9px;color:#555;text-decoration:none;padding:5px 9px}
.main-nav a.active{background:var(--orange);color:var(--white)}

.hero{position:relative;height:340px;background:linear-gradient(180deg,#8fc3ea 0%,#b9dbf2 30%,#3d5e8c 55%,#1f3558 100%)}
.hero-caption{position:absolute;left:60px;top:290px;background:rgba(0,0,0,.55);color:var(--white);font-size:13px;font-weight:600;padding:7px 12px}
.hero-arrow{position:absolute;top:158px;width:22px;height:22px;border-radius:50%;background:rgba(255,255,255,.75)}
.hero-arrow.prev{left:10px}.hero-arrow.next{right:10px}
.hero-arrow svg{display:block;margin:5px auto}

.welcome{text-align:center;padding:22px 56px 0}
.section-title{font-size:22px;font-weight:700;color:var(--ink)}
.section-title .accent{color:var(--orange)}
.welcome p{font-size:7.5px;line-height:1.6;color:var(--muted);margin-top:12px}

.benefits{display:flex;gap:22px;padding:26px 40px 0 56px}
.benefits-photo{width:160px;height:140px;background:linear-gradient(180deg,#9fcdf0 0%,#5b87b8 55%,#7fae3f 80%,#5f8f2a 100%);flex:none}
.benefits-body{flex:1}
.benefits-body h2{font-size:20px;font-weight:700}
.benefits-body .intro{font-size:7.5px;line-height:1.6;color:var(--muted);margin:8px 0 10px}
.benefit-list{display:grid;grid-template-columns:1fr 1fr;gap:4px 20px;list-style:none}
.benefit-list li{font-size:7px;color:var(--muted);padding-left:10px;position:relative}
.benefit-list li::before{content:"";position:absolute;left:0;top:3px;width:4px;height:4px;background:var(--orange)}

.cta-band{margin-top:36px;height:78px;background:var(--band);display:flex;align-items:center;justify-content:space-between;padding:0 56px}
.cta-band h3{font-size:12px;font-weight:600;color:var(--ink)}
.cta-band p{font-size:7.5px;color:var(--muted);margin-top:5px;line-height:1.5}
.cta-actions{display:flex;gap:12px}
.btn{font-size:9px;color:var(--white);padding:7px 14px;text-decoration:none}
.btn-primary{background:var(--orange)}
.btn-dark{background:#555}

.works{text-align:center;padding-top:22px}
.works-grid{display:flex;gap:12px;justify-content:center;margin-top:16px}
.work-photo{width:122px;height:100px}
.w1{background:linear-gradient(180deg,#a8d0ef,#4c5f73 60%,#6f5a44)}
.w2{background:linear-gradient(180deg,#bcdcf2,#3d5d8a 60%,#2b3e5c)}
.w3{background:linear-gradient(180deg,#9cc8ec,#7b5c3f 55%,#3b4e6a)}
.w4{background:linear-gradient(180deg,#9ec9ec,#2f4b78 60%,#1d3152)}
.dots{display:flex;gap:5px;justify-content:center;margin-top:10px}
.dots span{width:5px;height:5px;border-radius:50%;background:#bbb}
.dots span.on{background:var(--orange)}

.site-footer{position:absolute;top:1035px;left:0;width:673px;height:140px;background:var(--footer);display:grid;grid-template-columns:1.2fr 1fr 1.1fr 1.1fr;gap:20px;padding:18px 20px 0 56px;color:#aaa}
.site-footer h4{font-size:7.5px;color:var(--white);font-weight:600;margin-bottom:8px}
.site-footer p,.site-footer li{font-size:6.5px;line-height:1.6}
.site-footer ul{list-style:none}
.site-footer li::before{content:"› ";color:var(--orange)}
.contact-line{display:flex;gap:5px;align-items:center;font-size:6.5px;margin-bottom:3px}
.field{height:12px;background:#3b3b3b;margin-bottom:5px;font-size:6px;padding:2px 5px;color:#999}
.subscribe{display:inline-block;background:var(--orange);color:var(--white);font-size:6px;padding:3px 8px;float:right}
.bottom-bar{position:absolute;top:1175px;left:0;width:673px;height:25px;background:var(--footer-deep);display:flex;align-items:center;justify-content:space-between;padding:0 20px 0 56px;font-size:6px;color:#888}
.social{display:flex;gap:6px}
.social span{width:10px;height:10px;border-radius:50%;background:#555}
</style>
</head>
<body>
<div class="page">
  <header class="site-header">
    <div class="brand"><span class="brand-dot"></span>Veloria Energy</div>
    <nav class="main-nav">
      <a class="active" href="#">Home</a><a href="#">About Us</a><a href="#">Services</a><a href="#">Products</a><a href="#">Gallery</a><a href="#">Testimonials</a><a href="#">Contact Us</a>
    </nav>
  </header>

  <section class="hero" role="img" aria-label="Technician installing solar panels on a house roof under a blue sky">
    <span class="hero-arrow prev"><svg width="10" height="12" viewBox="0 0 10 12"><path d="M7 1 2 6l5 5" stroke="#555" stroke-width="2" fill="none"/></svg></span>
    <span class="hero-arrow next"><svg width="10" height="12" viewBox="0 0 10 12"><path d="M3 1l5 5-5 5" stroke="#555" stroke-width="2" fill="none"/></svg></span>
    <div class="hero-caption">AFFORDABLE solar and thermal heating applications</div>
  </section>

  <section class="welcome">
    <h1 class="section-title">Welcome To <span class="accent">Veloria Energy</span></h1>
    <p>Clean solar panels and thermal heating for every home, built to pay for themselves within one to three years. Our systems need very little sunlight, work with your existing water and heating, and run on fully renewable power. Lower your monthly bills, protect the environment and raise the resale value of your home with a simple, reliable system you can trust. Ask us about the 30% tax rebate on orders placed this year.</p>
  </section>

  <section class="benefits">
    <div class="benefits-photo" role="img" aria-label="Solar panel array on green grass under a blue sky"></div>
    <div class="benefits-body">
      <h2 class="section-title">Our Device <span class="accent">Benefits</span></h2>
      <p class="intro">Simple, effective and affordable. Every unit is designed to save you money from day one while keeping your home warm and powered.</p>
      <ul class="benefit-list">
        <li>Government 30% tax rebate if ordered by 2017</li><li>Low maintenance</li>
        <li>Solar panels from 40 - 90% efficient</li><li>Can be self installed</li>
        <li>Units pay for themselves</li><li>Saves the environment</li>
        <li>Works with existing water and heating systems</li><li>Zero emissions</li>
        <li>Lower energy consumption</li><li>Increases homes resale value</li>
        <li>Great backup heaters in a power outage</li><li>Great for remote locations</li>
        <li>100% solar powered, self running design</li><li>Increases jobs</li>
      </ul>
    </div>
  </section>

  <section class="cta-band">
    <div>
      <h3>Fusce convallis magna ac nibh tempor aliquam.</h3>
      <p>We sell very affordable panels and also provide backup in case of outage<br>and a low cost install to get started.</p>
    </div>
    <div class="cta-actions"><a class="btn btn-primary" href="#">Read More</a><a class="btn btn-dark" href="#">Contact Us</a></div>
  </section>

  <section class="works">
    <h2 class="section-title">Our <span class="accent">Works</span></h2>
    <div class="works-grid">
      <div class="work-photo w1" role="img" aria-label="House roof with installed solar panels"></div>
      <div class="work-photo w2" role="img" aria-label="Workers mounting solar panels on a roof"></div>
      <div class="work-photo w3" role="img" aria-label="Installer fitting a panel on a rooftop"></div>
      <div class="work-photo w4" role="img" aria-label="Close view of a rooftop solar array"></div>
    </div>
    <div class="dots"><span class="on"></span><span></span><span></span></div>
  </section>

  <footer class="site-footer">
    <div>
      <h4>WHO WE ARE</h4>
      <p>Veloria Energy brings affordable solar and thermal heating to homes and businesses. Our units are simple, clean and built to last, with friendly support from order to install.</p>
    </div>
    <div>
      <h4>USEFUL LINKS</h4>
      <ul><li>Home</li><li>About Us</li><li>Services</li><li>Products</li><li>Gallery</li><li>Testimonials</li><li>Contact Us</li></ul>
    </div>
    <div>
      <h4>GET IN TOUCH</h4>
      <p style="margin-bottom:6px">Reach our team for a free quote and a simple plan for your home.</p>
      <div class="contact-line"><svg width="7" height="8" viewBox="0 0 7 8"><path d="M3.5 0A3 3 0 0 0 .5 3c0 2.2 3 5 3 5s3-2.8 3-5a3 3 0 0 0-3-3z" fill="#f37122"/></svg>18 Harbor Lane, Springfield</div>
      <div class="contact-line"><svg width="7" height="7" viewBox="0 0 7 7"><path d="M1 0h2l.6 1.8-1 .8a4 4 0 0 0 1.8 1.8l.8-1L7 4v2c0 .6-.4 1-1 1A6 6 0 0 1 0 1c0-.6.4-1 1-1z" fill="#f37122"/></svg>(555) 014-2290</div>
      <div class="contact-line"><svg width="8" height="6" viewBox="0 0 8 6"><rect width="8" height="6" fill="#f37122"/><path d="M0 0l4 3 4-3" stroke="#2b2b2b" fill="none"/></svg>hello@veloriaenergy.com</div>
    </div>
    <div>
      <h4>CONTACT</h4>
      <p style="margin-bottom:5px">Subscribe for news, offers and rebate updates.</p>
      <div class="field">Name</div>
      <div class="field">Email</div>
      <span class="subscribe">SUBSCRIBE</span>
    </div>
  </footer>
  <div class="bottom-bar">
    <span>© 2017 Veloria Energy. All rights reserved.</span>
    <div class="social"><span></span><span></span><span></span><span></span></div>
  </div>
</div>
</body>
</html>
```